Crumb Crumb - Home baking business needs a business card design. I sell at artisan food festivals.

A design for rebranding my baking business which serves artisan food festivals in the UK. Produce is locally sourced, homegrown or foraged, I make rustic unusual recipes. I would like a simple design using classic colours. I like green, 'Hadley and Stone". I like chunky lettering, but very open to new ideas/designs. On the reverse side I would like a singular symbol demonstrating baking either a bowl and wooden spoon or cake and the facebook icon with CrumbCrumb
Updates

Project Deadline Extended
Reason: I would like to progress with the design by Jen Marlow 4827306 . I misunderstood the deadline itinerary but would very much like to go ahead with your design. thanks

Target Market(s)

customers at food festivals, other small food businesses

Industry/Entity Type

Business

Contact Information for Business Card

Minimal amount of type on the card. Design to accentuate the look of my stall and style of baking . I display cakes on either old slate tiles, old palette boxes. Prices are hand written on brown luggage labels

Font styles to use
Other font styles liked:
• Blair MdiTC

Requirements
Must have
• Underneath Crumb Crumb i would like to have homemade by Pam somewhere on the front of the card.
Nice to have
• Clear lettering, classic colours i.e. Hadley and Stone colour palettes.
Should not have
• Fancy, blingy, wordy,

```html
<!DOCTYPE html>
<html lang="en">
<head>
<meta charset="utf-8">
<title>CrumbCrumb — Business Card</title>
<link rel="stylesheet" href="https://fonts.googleapis.com/css2?family=Josefin+Sans:wght@600;700&family=Sacramento&display=swap">
<style>
  :root {
    --page-bg: #3a2b23;
    --mint-light: #a9dbc6;
    --mint-mid: #8fceb4;
    --mint-deep: #76bfa1;
    --card-white: #fbfbf9;
    --text-white: #ffffff;
    --text-grey: #5a5a5a;
    --apron-mint: #7fcfb4;
    --apron-deep: #5fb898;
    --apron-tie: #e3a83a;
  }
  * { box-sizing: border-box; margin: 0; padding: 0; }
  html, body {
    width: 1200px;
    height: 1000px;
    overflow: hidden;
    background: var(--page-bg);
  }
  .canvas {
    position: relative;
    width: 1200px;
    height: 1000px;
  }
  .card {
    position: absolute;
    left: 290px;
    width: 620px;
    height: 370px;
    box-shadow: 0 6px 18px rgba(0,0,0,0.45);
  }
  .card-front {
    top: 75px;
    background:
      radial-gradient(ellipse at 30% 30%, rgba(255,255,255,0.18), transparent 55%),
      radial-gradient(ellipse at 70% 70%, var(--mint-deep), transparent 60%),
      linear-gradient(160deg, var(--mint-mid), var(--mint-light) 50%, var(--mint-mid));
    display: flex;
    flex-direction: column;
    align-items: center;
  }
  .brand-name {
    margin-top: 130px;
    font-family: "Josefin Sans", sans-serif;
    font-weight: 700;
    font-size: 64px;
    letter-spacing: 4px;
    color: var(--text-white);
    text-shadow: 1px 2px 3px rgba(0,0,0,0.25);
    line-height: 1;
  }
  .tagline {
    margin-top: 28px;
    font-family: "Sacramento", cursive;
    font-size: 42px;
    color: var(--text-white);
    line-height: 1;
  }
  .card-back {
    top: 520px;
    background: var(--card-white);
    display: flex;
    flex-direction: column;
    align-items: center;
  }
  .apron-illustration {
    margin-top: 30px;
    width: 210px;
    height: 250px;
  }
  .social-handle {
    margin-top: 22px;
    display: flex;
    align-items: center;
    gap: 12px;
  }
  .social-dot {
    width: 22px;
    height: 22px;
    border-radius: 50%;
    background: var(--text-grey);
  }
  .social-name {
    font-family: "Josefin Sans", sans-serif;
    font-weight: 600;
    font-size: 24px;
    letter-spacing: 3px;
    color: var(--text-grey);
    line-height: 1;
    padding-top: 4px;
  }
</style>
</head>
<body>
  <main class="canvas">
    <section class="card card-front">
      <h1 class="brand-name">CRUMBCRUMB</h1>
      <p class="tagline">Homemade by Pam</p>
    </section>

    <section class="card card-back">
      <svg class="apron-illustration" viewBox="0 0 210 250" role="img" aria-label="Watercolour illustration of a mint green apron with golden ties">
        <defs>
          <linearGradient id="apronFill" x1="0" y1="0" x2="0" y2="1">
            <stop offset="0" stop-color="var(--apron-mint)"/>
            <stop offset="1" stop-color="var(--apron-deep)"/>
          </linearGradient>
        </defs>
        <rect x="35" y="10" width="140" height="230" rx="10" fill="url(#apronFill)" opacity="0.85"/>
      </svg>
      <div class="social-handle">
        <span class="social-dot"></span>
        <span class="social-name">CRUMBCRUMB</span>
      </div>
    </section>
  </main>
</body>
</html>
```